Website/Logo Design

We need a logo and website design for an opinion mining startup called VantaLume. Our technology mines the web to automatically discover what people are saying about brands, products, etc. The project we are fielding here is for our informational, public-facing website. In its initial incarnation, it will simply be a vehicle for marketing materials and information on our company and its offerings, but it should be flexible enough to expand as more content/functionality is added.

Some designs we like are:
http://www.tradewhisk.example
http://www.gorvantel.example
http://www.kfz.example
http://www.lintwharf.example
http://moxbarrel.example
http://trundlemq.example
http://www.zopla.example
Updates

All, please try to shy away from using a photo of a person as the focal point of the design.  Our company is more technological than social.

Target Market(s)

Primarily businesses interested in sentiment analysis (typically companies involved in advertising, market research, PR, etc.)

Industry/Entity Type

It Company

Requirements
Must have
• We are looking for a clean, modern, and professional design. This includes a logo, homepage, and internal page if it will differ from the homepage.
Nice to have
• It would be excellent if you could provide an HTML mockup if your design is chosen.
Should not have
• Flash, excessive bells and whistles

```html
<!DOCTYPE html>
<html lang="en">
<head>
<meta charset="utf-8">
<title>VantaLume – Website and Logo</title>
<link rel="stylesheet" href="https://fonts.googleapis.com/css2?family=Open+Sans:ital,wght@0,400;0,600;0,700;1,400&display=swap">
<style>
:root{
  --navy:#0d3a5f;
  --navy-deep:#082a47;
  --ink:#1f2a36;
  --text:#3a3a3a;
  --heading:#123f66;
  --gold:#e0a32a;
  --gold-btn:#d9a032;
  --slate-btn:#6f84a3;
  --panel:#f1f1f1;
  --rule:#c9c9c9;
  --footer:#333333;
  --footer-text:#a9a9a9;
  --white:#ffffff;
}
*{margin:0;padding:0;box-sizing:border-box}
html,body{width:1200px;height:2722px;overflow:hidden;background:var(--white)}
body{position:relative;font-family:"Open Sans",Verdana,sans-serif;color:var(--text)}
.abs{position:absolute}
p{font-size:10.5px;line-height:16px}

/* header */
.site-header{position:absolute;left:0;width:1200px;height:156px;background:linear-gradient(#ffffff,#ececec)}
.brand{position:absolute;display:flex;align-items:center;gap:10px}
.brand-mark{width:22px;height:22px;background:var(--navy)}
.brand-name{font-weight:600;color:#3b3f45;letter-spacing:-1px}
.main-nav{position:absolute;font-size:14px;color:var(--ink)}
.main-nav span{position:absolute;white-space:nowrap}
.main-nav .current{color:var(--gold)}

/* buttons */
.btn{position:absolute;display:flex;align-items:center;justify-content:center;color:var(--white);font-size:11px;font-weight:600;border-radius:2px}
.btn-slate{background:linear-gradient(#8799b4,#5d7192)}
.btn-gold{background:linear-gradient(#e8b54a,#c98c1f)}
.btn-mini{font-size:7px}

/* hero */
.hero{position:absolute;left:0;top:152px;width:1200px;height:271px;background:linear-gradient(90deg,var(--navy-deep),var(--navy) 60%,#164a75)}
.hero-card{position:absolute;left:190px;top:152px;width:360px;height:303px;background:var(--white);border-radius:10px;box-shadow:0 2px 6px rgba(0,0,0,.25)}
.hero-photo{position:absolute;left:13px;top:5px;width:337px;height:234px;border-radius:8px;background:linear-gradient(135deg,#f4f6f9,#c7d3e2 55%,#7f97b6)}
.hero-title{position:absolute;left:618px;top:196px;font-size:25px;font-weight:600;color:var(--white)}
.hero-title em{font-style:normal;color:var(--gold)}
.hero-copy{position:absolute;left:618px;top:236px;width:505px;color:#dfe8f1;font-size:10px;line-height:17px}

/* content panel */
.panel{position:absolute;left:0;width:1200px;background:var(--panel)}
.feature{position:absolute;top:487px;width:279px;height:143px;background:var(--white);border-radius:10px 10px 0 0;background:linear-gradient(#ffffff,#f7f7f7)}
.feature h3{position:absolute;left:20px;top:12px;font-size:18px;font-weight:700;color:var(--gold)}
.feature p{position:absolute;left:30px;top:44px;width:230px;font-size:9px;line-height:14px}
.feature .btn{right:20px;top:114px;width:65px;height:17px}
.hrule{position:absolute;height:1px;background:var(--rule)}
.vrule{position:absolute;width:1px;background:var(--rule)}
.col-title{position:absolute;font-size:16px;font-weight:700;color:var(--heading)}
.bullets{position:absolute;list-style:none}
.bullets li{position:relative;padding-left:28px;font-size:10.5px;height:25.5px;line-height:16px;color:var(--text)}
.bullets svg{position:absolute;left:0;top:3px}
.quote{position:absolute;left:760px;width:272px;font-size:10px;line-height:16px;font-style:italic}
.quote .mark{position:absolute;left:0;top:-4px;color:var(--gold);font-size:20px;font-style:normal}
.quote p{padding-left:16px;font-size:10px}
.quote .who{text-align:right;font-style:normal;color:var(--heading);margin-top:4px}

/* footer */
.site-footer{position:absolute;left:0;width:1200px;background:var(--footer);font-size:13px;color:var(--footer-text)}
.site-footer span{position:absolute;white-space:nowrap}

/* inner page */
.inner-band{position:absolute;left:0;top:1316px;width:1200px;height:32px;background:linear-gradient(var(--navy),var(--navy-deep))}
.inner-photo{position:absolute;left:387px;top:1416px;width:184px;height:146px;background:linear-gradient(135deg,#3a3f95,#d8c24a 50%,#2a3a86)}
.form-label{position:absolute;left:631px;font-size:10px;font-style:italic;color:var(--heading)}
.form-field{position:absolute;left:631px;background:var(--white);border:1px solid #e2e2e2}

/* logo sheet */
.logo-sheet{position:absolute;left:0;top:2211px;width:853px;height:511px;background:radial-gradient(ellipse at 40% 20%,#ffffff,#e9e9e9 75%)}
.logo-dark{position:absolute;left:853px;top:2211px;width:347px;height:226px;background:#000}
</style>
</head>
<body>

<!-- Home page -->
<header class="site-header" style="top:0">
  <div class="brand" style="left:186px;top:50px">
    <span class="brand-mark"></span><span class="brand-name" style="font-size:40px">VantaLume</span>
  </div>
  <nav class="main-nav" style="top:129px;left:0">
    <span class="current" style="left:601px">Home</span>
    <span style="left:673px">About Us</span>
    <span style="left:766px">Features</span>
    <span style="left:855px">Case Studies</span>
    <span style="left:971px">Contact Us</span>
  </nav>
</header>

<section class="hero" aria-label="Introduction"></section>
<div class="hero-card">
  <div class="hero-photo" role="img" aria-label="Close-up of an email inbox menu beside a rising line chart"></div>
  <span class="btn btn-slate" style="left:220px;top:254px;width:115px;height:28px;font-size:13px">Learn More</span>
</div>
<h1 class="hero-title">Their Opinion <em>Your results</em></h1>
<p class="hero-copy">Lorem ipsum dolor sit amet, consectetur adipiscing elit. Nunc at ligula sed purus blandit egestas ut eu nulla. Etiam scelerisque elit sed mi laoreet tempus. Cras risus mauris, laoreet ut scelerisque a, sagittis non augue. Vestibulum ante ipsum primis in faucibus orci luctus et ultrices posuere cubilia Curae; Aenean eu ante mauris. Cum sociis natoque penatibus et magnis dis parturient montes, nascetur ridiculus mus.</p>
<span class="btn btn-gold" style="left:614px;top:360px;width:106px;height:29px;font-size:12px">Learn More</span>

<section class="panel" style="top:465px;height:462px">
</section>
<div class="feature" style="left:161px"><h3>Top Features</h3><p>Lorem ipsum dolor sit amet, consectetur adipiscing elit. Nunc at ligula sed purus blandit egestas ut eu nulla. Etiam scelerisque elit sed mi laoreet tempus. Cras risus mauris, laoreet ut scelerisque a, sagittis non augue.</p><span class="btn btn-slate btn-mini">Learn more</span></div>
<div class="feature" style="left:457px"><h3>Where To Start?</h3><p>Lorem ipsum dolor sit amet, consectetur adipiscing elit. Nunc at ligula sed purus blandit egestas ut eu nulla. Etiam scelerisque elit sed mi laoreet tempus. Cras risus mauris, laoreet ut scelerisque a, sagittis non augue.</p><span class="btn btn-slate btn-mini">Learn more</span></div>
<div class="feature" style="left:753px"><h3>Top Features</h3><p>Lorem ipsum dolor sit amet, consectetur adipiscing elit. Nunc at ligula sed purus blandit egestas ut eu nulla. Etiam scelerisque elit sed mi laoreet tempus. Cras risus mauris, laoreet ut scelerisque a, sagittis non augue.</p><span class="btn btn-slate btn-mini">Learn more</span></div>
<div class="hrule" style="left:161px;top:641px;width:876px"></div>
<div class="vrule" style="left:444px;top:662px;height:252px"></div>
<div class="vrule" style="left:741px;top:662px;height:252px"></div>

<h2 class="col-title" style="left:167px;top:683px">What It Can Do For You</h2>
<p class="abs" style="left:167px;top:718px;width:265px">Lorem ipsum dolor sit amet, consectetur adipiscing elit. Nunc at ligula sed purus blandit egestas ut eu nulla. Etiam scelerisque elit sed mi laoreet tempus. Cras risus mauris, laoreet ut scelerisque a, sagittis non augue. Vestibulum ante ipsum primis in faucibus orci luctus et ultrices posuere cubilia Curae; Aenean eu ante mauris. Cum sociis natoque penatibus et magnis dis parturient montes, nascetur ridiculus mus.</p>
<span class="btn btn-slate btn-mini" style="left:372px;top:887px;width:64px;height:18px">Learn More</span>

<h2 class="col-title" style="left:461px;top:683px">Key Concepts</h2>
<ul class="bullets" style="left:461px;top:718px">
  <li><svg width="16" height="10" viewBox="0 0 16 10"><path d="M0 3h9V0l7 5-7 5V7H0z" fill="#3b73b5"/></svg>Morbi venenatis dolor non magna rutrum</li>
  <li><svg width="16" height="10" viewBox="0 0 16 10"><path d="M0 3h9V0l7 5-7 5V7H0z" fill="#3b73b5"/></svg>Sed vehicula ornare tortor</li>
  <li><svg width="16" height="10" viewBox="0 0 16 10"><path d="M0 3h9V0l7 5-7 5V7H0z" fill="#3b73b5"/></svg>Pellentesque vel neque ut ipsum convallis</li>
  <li><svg width="16" height="10" viewBox="0 0 16 10"><path d="M0 3h9V0l7 5-7 5V7H0z" fill="#3b73b5"/></svg>Aenean quam risus</li>
  <li><svg width="16" height="10" viewBox="0 0 16 10"><path d="M0 3h9V0l7 5-7 5V7H0z" fill="#3b73b5"/></svg>Integer ullamcorper posuere nulla ac ultrices</li>
</ul>

<h2 class="col-title" style="left:760px;top:683px">Testimonials</h2>
<blockquote class="quote" style="top:710px"><span class="mark">“</span><p>Lorem ipsum dolor sit amet, consectetur adipiscing elit. Nunc at ligula sed purus blandit egestas ut eu nulla. Etiam scelerisque elit sed mi laoreet tempus.</p><p class="who">Dara Quill</p></blockquote>
<blockquote class="quote" style="top:822px"><span class="mark">“</span><p>Lorem ipsum dolor sit amet, consectetur adipiscing elit. Nunc at ligula sed purus blandit egestas ut eu nulla. Etiam scelerisque elit sed mi laoreet tempus.</p><p class="who">Milo Brant - Kesto Tech</p></blockquote>

<footer class="site-footer" style="top:927px;height:233px">
  <span style="left:167px;top:24px;font-size:12px">Copyright VantaLume  All Rights Reserved</span>
  <span style="left:508px;top:24px">Home</span><span style="left:572px;top:24px">/</span>
  <span style="left:603px;top:24px">About Us</span><span style="left:688px;top:24px">/</span>
  <span style="left:717px;top:24px">Features</span><span style="left:798px;top:24px">/</span>
  <span style="left:827px;top:24px">Case Studies</span><span style="left:932px;top:24px">/</span>
  <span style="left:965px;top:24px">Contact Us</span>
</footer>

<!-- Inner page -->
<header class="site-header" style="top:1160px">
  <div class="brand" style="left:186px;top:52px">
    <span class="brand-mark"></span><span class="brand-name" style="font-size:40px">VantaLume</span>
  </div>
  <nav class="main-nav" style="top:130px;left:0">
    <span class="current" style="left:601px">Home</span>
    <span style="left:673px">About Us</span>
    <span style="left:766px">Features</span>
    <span style="left:855px">Case Studies</span>
    <span style="left:971px">Contact Us</span>
  </nav>
</header>
<div class="inner-band"></div>
<section class="panel" style="top:1348px;height:620px"></section>

<h2 class="col-title" style="left:167px;top:1412px;width:210px;line-height:21px">Lorem ipsum dolor sit amet, consectetur adipiscing elit.</h2>
<div class="inner-photo" role="img" aria-label="Laptop keyboard glowing with golden light"></div>
<p class="abs" style="left:167px;top:1486px;width:210px">Nunc at ligula sed purus blandit egestas ut eu nulla. Etiam scelerisque elit sed mi laoreet tempus. Cras risus</p>
<p class="abs" style="left:167px;top:1566px;width:405px">mauris, laoreet ut scelerisque a, sagittis non augue. Vestibulum ante ipsum primis in faucibus orci luctus et ultrices posuere cubilia Curae; Aenean eu ante mauris. Cum sociis natoque penatibus et magnis dis parturient montes, nascetur ridiculus mus. Quisque lobortis porta ligula, eget consectetur metus semper sit amet. Mauris cursus turpis eu enim euismod malesuada. Nam consectetur augue ac nulla mattis tristique. Pellentesque congue commodo libero, a placerat neque tristique nec. Nullam malesuada nulla non risus vehicula molestie. Integer sed ligula urna. In in turpis erat, at hendrerit diam.</p>
<ul class="bullets" style="left:167px;top:1780px">
  <li><svg width="16" height="10" viewBox="0 0 16 10"><path d="M0 3h9V0l7 5-7 5V7H0z" fill="#3b73b5"/></svg>Morbi venenatis dolor non magna rutrum</li>
  <li><svg width="16" height="10" viewBox="0 0 16 10"><path d="M0 3h9V0l7 5-7 5V7H0z" fill="#3b73b5"/></svg>Sed vehicula ornare tortor</li>
  <li><svg width="16" height="10" viewBox="0 0 16 10"><path d="M0 3h9V0l7 5-7 5V7H0z" fill="#3b73b5"/></svg>Pellentesque vel neque ut ipsum convallis</li>
  <li><svg width="16" height="10" viewBox="0 0 16 10"><path d="M0 3h9V0l7 5-7 5V7H0z" fill="#3b73b5"/></svg>Aenean quam risus</li>
  <li><svg width="16" height="10" viewBox="0 0 16 10"><path d="M0 3h9V0l7 5-7 5V7H0z" fill="#3b73b5"/></svg>Integer ullamcorper posuere nulla ac ultrices</li>
</ul>
<div class="vrule" style="left:595px;top:1400px;height:525px"></div>

<h2 class="col-title" style="left:614px;top:1412px">Lorem ipsum dolor sit amet</h2>
<p class="abs" style="left:614px;top:1452px;width:420px">Nunc at ligula sed purus blandit egestas ut eu nulla. Etiam scelerisque elit sed mi laoreet tempus. Cras risus mauris, laoreet ut scelerisque a, sagittis non augue. Vestibulum ante ipsum primis in faucibus orci luctus et ultrices posuere cubilia Curae; Aenean eu ante mauris. Cum sociis natoque penatibus et magnis dis parturient montes, nascetur ridiculus mus. Quisque lobortis porta ligula, eget consectetur metus semper sit amet. Mauris cursus turpis eu enim euismod malesuada. Nam consectetur augue ac nulla mattis tristique. Pellentesque congue commodo libero, a placerat neque tristique nec. Nullam malesuada nulla non risus vehicula molestie. Integer sed ligula urna. In in turpis erat, at hendrerit diam.</p>
<form aria-label="Contact form">
  <label class="form-label" style="top:1668px">Name</label>
  <span class="form-field" style="top:1686px;width:232px;height:20px"></span>
  <label class="form-label" style="top:1712px">Email</label>
  <span class="form-field" style="top:1729px;width:232px;height:21px"></span>
  <label class="form-label" style="top:1755px">Message</label>
  <span class="form-field" style="top:1773px;width:285px;height:127px"></span>
  <span class="btn btn-slate btn-mini" style="left:631px;top:1913px;width:71px;height:17px">Submit</span>
</form>

<footer class="site-footer" style="top:1968px;height:207px">
  <span style="left:167px;top:28px;font-size:12px">Copyright VantaLume  All Rights Reserved</span>
  <span style="left:508px;top:28px">Home</span><span style="left:572px;top:28px">/</span>
  <span style="left:603px;top:28px">About Us</span><span style="left:688px;top:28px">/</span>
  <span style="left:717px;top:28px">Features</span><span style="left:798px;top:28px">/</span>
  <span style="left:827px;top:28px">Case Studies</span><span style="left:932px;top:28px">/</span>
  <span style="left:965px;top:28px">Contact Us</span>
</footer>

<!-- Logo sheet -->
<section class="logo-sheet" aria-label="Logo on light background">
  <div class="brand" style="left:160px;top:190px;gap:18px">
    <span class="brand-mark" style="width:46px;height:46px"></span><span class="brand-name" style="font-size:92px;letter-spacing:-3px">VantaLume</span>
  </div>
</section>
<section class="logo-dark" aria-label="Logo reversed on black">
  <div class="brand" style="left:70px;top:88px;gap:8px">
    <span class="brand-mark" style="width:16px;height:16px;background:#fff"></span><span class="brand-name" style="font-size:32px;color:#fff">VantaLume</span>
  </div>
</section>
<section class="abs" style="left:853px;top:2437px;width:347px;height:285px;background:#fff" aria-label="Logo in single colour">
  <div class="brand" style="left:70px;top:100px;gap:8px">
    <span class="brand-mark" style="width:16px;height:16px;background:#000"></span><span class="brand-name" style="font-size:32px;color:#000">VantaLume</span>
  </div>
</section>

</body>
</html>
```